Redesign website for small print company

Vindaborgprent is a small printing company in Iceland mainly servicing Students, schools, etc. We are also doing all kind of other jobs, like business cards, book printing, brochure printing etc. We are also selling books online.
Our website is: www.vindaborgprent.is
What we are looking for is:
- Web Design (Uncoded - PSD layout only)
- Mobile friendly design, using our current color scheme: Red, green, yellow and light gray.
- Clean simple design
- Simple, light and easy to use.
- More menu Items/drop down
Industry/Entity Type
Digital Printing
Number of Pages Required
5+ page
Requirements
Must have
- Easy navigation
- Designed for mobile
- Current color scheme (see logo)
Nice to have
- Icon based products

```html
<!DOCTYPE html>
<html lang="en">
<head>
<meta charset="utf-8">
<title>Vindaborgprent – Printing solutions</title>
<link href="https://fonts.googleapis.com/css2?family=Poppins:wght@300;400;500;600;700&family=Noto+Serif:wght@400&display=swap" rel="stylesheet">
<style>
:root{
  --red:#e42a2a;
  --green:#1b5b2b;
  --yellow:#fbd800;
  --ink:#1d1d1d;
  --text:#555;
  --muted:#9aa0a6;
  --line:#e6e8eb;
  --placeholder:#eef2f6;
  --dark:#262424;
  --white:#fff;
}
*{box-sizing:border-box;margin:0;padding:0}
html,body{width:1200px;height:3061px;overflow:hidden;background:var(--white)}
body{position:relative;font-family:"Poppins",sans-serif;color:var(--text);font-size:12px}
.abs{position:absolute}
.row{display:flex;align-items:center}

/* header */
.topbar{top:8px;left:88px;width:1024px;height:20px;font-size:12px;color:var(--ink);justify-content:space-between}
.topbar .row span{margin-right:26px;display:flex;align-items:center;gap:6px}
.brand{top:36px;left:0;width:1200px;justify-content:center;gap:8px}
.brand-dot{width:12px;height:12px;border-radius:50%;background:var(--muted)}
.brand-name{font-weight:500;font-size:20px;color:var(--ink)}
.locale{top:76px;left:88px;font-size:12px;color:var(--muted);gap:8px}
.flag{width:14px;height:14px;border-radius:50%;background:var(--red)}
.tools{top:72px;left:996px;gap:10px}
.tool{width:34px;height:28px;border-radius:14px;background:var(--yellow);display:flex;align-items:center;justify-content:center}
.avatar{width:26px;height:26px;border-radius:50%;background:linear-gradient(135deg,#c9805b,#7a4c3a)}
.mainnav{top:126px;left:0;width:1200px;height:52px;border-top:1px solid var(--line);border-bottom:1px solid var(--line)}
.mainnav a{position:absolute;top:16px;font-size:13px;color:var(--ink);text-decoration:none}
.giftcards{top:14px!important;background:var(--red);color:var(--white)!important;font-weight:600;padding:2px 14px}

/* hero */
.hero-copy{top:252px;left:347px;width:240px;font-size:26px;color:#555;line-height:1.25;font-weight:300;z-index:2}
.hero-copy span{display:block;padding-left:30px}
.action{top:346px;width:80px;text-align:center;font-size:9px;font-weight:600;color:var(--ink)}
.action .disc{width:70px;height:70px;border-radius:50%;margin:0 auto 8px;display:flex;align-items:center;justify-content:center}
.hero-photo{top:226px;left:604px;width:240px;height:280px;background:linear-gradient(180deg,#f4f5f7,#dfe3ea);border-radius:6px}
.eco-badge{top:222px;left:856px;width:34px;height:34px;border-radius:50%;background:var(--green)}

/* products */
.section-title{left:0;width:1200px;text-align:center;font-weight:600;font-size:30px;color:var(--ink)}
.rule{left:565px;width:70px;height:2px;background:var(--red)}
.section-sub{left:0;width:1200px;text-align:center;font-size:13px;line-height:1.75;color:#666}
.card{top:694px;width:285px;height:432px;border:1px solid #f1f2f4;box-shadow:0 2px 6px rgba(0,0,0,.05);text-align:center}
.card-img{height:200px;background:var(--placeholder);display:flex;align-items:center;justify-content:center;font-weight:700;font-size:26px;color:#e1e6ec}
.btn-small{display:inline-block;background:var(--green);color:var(--white);font-size:8px;font-weight:600;padding:6px 22px;margin-top:-10px}
.card h3{font-size:15px;font-weight:600;color:var(--ink);margin-top:32px}
.card .mini-rule{width:36px;height:1px;background:var(--ink);margin:14px auto}
.card p{font-size:9px;line-height:1.6;color:#8a8f95;padding:0 40px;height:58px;overflow:hidden}
.card .spread{font-size:9px;color:#8a8f95;margin-top:20px}
.dots{justify-content:center;gap:30px;margin-top:14px}
.dot{width:8px;height:8px;border-radius:50%;background:#b4b9be}
.view-all{top:1162px;left:776px;font-size:23px;font-weight:600;color:var(--ink);gap:14px}

/* feature blocks */
.quote-block{top:1245px;left:88px;width:506px;height:412px;background:linear-gradient(180deg,var(--yellow) 0 41%,var(--red) 41% 100%)}
.quote-box{position:absolute;top:41px;left:51px;width:402px;height:281px;background:var(--white);padding:62px 0 0 36px}
.quote-box p{font-size:37px;font-weight:700;line-height:1.2;color:var(--green)}
.tweet{position:absolute;top:332px;left:0;width:100%;text-align:center;color:var(--white);font-size:15px;font-weight:500}
.tweet i{display:block;width:20px;height:20px;border-radius:50%;background:var(--white);margin:0 auto 10px}
.learn-block{top:1245px;left:604px;width:508px;height:412px;background:linear-gradient(160deg,#5b544f,#2e2a28 60%,#3c3633);text-align:center;color:var(--white)}
.learn-block h2{font-family:"Noto Serif",serif;font-weight:400;font-size:29px;margin-top:116px}
.learn-block p{font-size:9px;line-height:1.6;color:#ddd;margin-top:44px}
.btn-yellow{display:inline-block;background:var(--yellow);color:var(--ink);font-size:8px;font-weight:600;padding:8px 30px;margin-top:24px}

/* subscribe */
.subscribe{top:1690px;left:88px;width:1024px;height:140px;border:1px solid #eceef0;box-shadow:0 2px 6px rgba(0,0,0,.05)}
.subscribe-photo{position:absolute;left:0;top:0;width:502px;height:138px;background:linear-gradient(100deg,#f3f3f3,#e2e2e2 55%,#f5f5f5)}
.subscribe h4{position:absolute;left:516px;top:36px;font-size:13px;font-weight:500;color:#777;letter-spacing:.5px}
.subscribe small{position:absolute;left:516px;top:56px;font-size:9px;color:var(--muted)}
.email-field{position:absolute;left:516px;top:94px;width:192px;height:24px;border-bottom:1px solid var(--line);font-size:10px;color:#888;display:flex;align-items:center;gap:8px;padding-left:12px}
.btn-subscribe{position:absolute;left:720px;top:94px;width:90px;height:26px;background:var(--green);color:var(--white);font-size:8px;font-weight:600;display:flex;align-items:center;justify-content:center}

/* instagram */
.insta{top:2026px;width:174px;height:229px;border:1px solid #f0f1f3;box-shadow:0 2px 6px rgba(0,0,0,.05)}
.insta-img{height:170px;background:var(--placeholder);display:flex;align-items:center;justify-content:center;font-weight:700;font-size:17px;color:#e1e6ec}
.insta-cap{display:flex;gap:10px;padding:12px 12px 0 18px;font-size:8px;line-height:1.4;color:#666}
.insta-cap i{flex:none;width:9px;height:9px;border:1px solid #999;margin-top:6px}
.insta-cap b{color:#2f6fc2;font-weight:500}

/* contact */
.contact-dark{top:2338px;left:88px;width:594px;height:176px;background:var(--dark);color:var(--white);font-size:8px;line-height:1.7}
.contact-dark h5{font-size:8.5px;font-weight:600;margin-bottom:10px}
.contact-col{position:absolute;top:36px}
.map{top:2514px;left:88px;width:594px;height:224px;background:linear-gradient(135deg,#eeeeee,#e4e6e3)}
.form{top:2368px;left:728px;width:240px}
.form h4{font-size:14px;font-weight:500;color:var(--ink);line-height:1.3;width:340px}
.form label{display:block;font-size:8px;color:#999;margin-top:14px}
.field{height:22px;border:1px solid #dcdfe2;margin-top:4px;font-size:8px;color:#555;padding:5px 8px}
.field.tall{height:62px}
.form .call{font-size:8px;color:#2f6fc2;margin-top:22px}
.btn-send{width:86px;height:24px;background:var(--green);color:var(--white);font-size:8px;font-weight:600;display:flex;align-items:center;justify-content:center;margin-top:20px}

/* partners + footer */
.partners{top:2770px;left:88px;width:1024px;justify-content:space-between;color:#a9adb2;font-size:17px;font-weight:500}
.footer-rule{top:2826px;left:88px;width:1024px;height:1px;background:var(--line)}
.footer-col{top:2852px;font-size:8px;line-height:2.35;color:#555}
.footer-col h6{font-size:8px;font-weight:600;color:var(--ink);letter-spacing:.4px}
.footer-social{top:2890px;left:972px;gap:12px}
.footer-social .dot{width:9px;height:9px;background:#aaa}
.copyright{top:2930px;left:918px;font-size:7.5px;color:#999}
</style>
</head>
<body>

<header>
  <div class="abs row topbar">
    <div class="row">
      <span><svg width="10" height="10" viewBox="0 0 10 10"><path d="M2 1l2 2-1 1.5c.8 1.3 1.5 2 2.5 2.5L7 6l2 2-1.5 1.5C4.5 9 1 5.5.5 2.5z" fill="#333"/></svg>555 0142</span>
      <span><svg width="11" height="8" viewBox="0 0 11 8"><rect width="11" height="8" fill="#333"/><path d="M0 0l5.5 4L11 0" stroke="#fff" fill="none"/></svg>verk@vindaborgprent.is</span>
    </div>
    <div class="row" style="gap:6px"><svg width="10" height="10" viewBox="0 0 10 10"><circle cx="5" cy="5" r="4" fill="none" stroke="#333"/><path d="M5 2.5V5l1.8 1" stroke="#333" fill="none"/></svg>Mon - Fri: 9-17</div>
  </div>

  <div class="abs row brand"><span class="brand-dot"></span><span class="brand-name">Vindaborgprent</span></div>

  <div class="abs row locale"><span class="flag"></span>English - UK &#8964;</div>
  <div class="abs row tools">
    <span class="tool"><svg width="12" height="12" viewBox="0 0 12 12"><circle cx="5" cy="5" r="3.5" fill="none" stroke="#333" stroke-width="1.5"/><path d="M7.5 7.5l3 3" stroke="#333" stroke-width="1.5"/></svg></span>
    <span class="tool"><svg width="13" height="12" viewBox="0 0 13 12"><path d="M1 1h2l1.5 7h6.5l1-5H4" fill="none" stroke="#333" stroke-width="1.3"/><circle cx="5.5" cy="10.5" r="1" fill="#333"/><circle cx="10" cy="10.5" r="1" fill="#333"/></svg></span>
    <span class="avatar" role="img" aria-label="Account profile photo"></span>
  </div>

  <nav class="abs mainnav">
    <a style="left:106px">Home</a>
    <a style="left:190px">Popular &#8963;</a>
    <a style="left:296px">Shop &#8964;</a>
    <a style="left:377px">Job Submit</a>
    <a style="left:486px">About Us</a>
    <a class="giftcards" style="left:932px">Gift Cards</a>
    <a style="left:1037px;color:#777">Find a store</a>
  </nav>
</header>

<section class="hero">
  <div class="abs hero-copy">Engar áhyggjur<span>... þetta reddast</span></div>
  <div class="abs action" style="left:322px">
    <div class="disc" style="background:var(--red)"><svg width="30" height="26" viewBox="0 0 30 26"><rect x="1" y="6" width="28" height="19" rx="3" fill="#fff"/><rect x="10" y="1" width="10" height="7" rx="2" fill="none" stroke="#fff" stroke-width="2.5"/></svg></div>SENDA VERK</div>
  <div class="abs action" style="left:404px">
    <div class="disc" style="background:var(--yellow)"><svg width="30" height="26" viewBox="0 0 30 26"><ellipse cx="15" cy="13" rx="14" ry="11" fill="#333"/><circle cx="9" cy="9" r="2.5" fill="var(--yellow)"/><circle cx="16" cy="7" r="2.5" fill="var(--yellow)"/><circle cx="22" cy="12" r="2.5" fill="var(--yellow)"/></svg></div>HANNA VERK</div>
  <div class="abs action" style="left:492px">
    <div class="disc" style="background:var(--green);color:#fff;font-size:38px;font-weight:700">?</div>FÁ TILBOÐ</div>
  <div class="abs hero-photo" role="img" aria-label="Group of cheerful students holding books and printed papers"></div>
  <div class="abs eco-badge"></div>
</section>

<section class="products">
  <h1 class="abs section-title" style="top:556px">Providing the best printing solutions</h1>
  <div class="abs rule" style="top:612px"></div>
  <p class="abs section-sub" style="top:630px">We print superb quality goods on a range of 100% recycled papers<br>and boards. Check out some of our popular products</p>

  <article class="abs card" style="left:127px">
    <div class="card-img">IMAGE HERE</div><span class="btn-small">SEE MORE</span>
    <h3>ART PRINTS</h3><div class="mini-rule"></div>
    <p>Fine art prints on heavy matte stock, made to last for years with rich colour and sharp detail for any wall you have.</p>
    <div class="spread">Spread the words</div><div class="row dots"><i class="dot"></i><i class="dot"></i><i class="dot"></i></div>
  </article>
  <article class="abs card" style="left:445px">
    <div class="card-img">IMAGE HERE</div><span class="btn-small">SEE MORE</span>
    <h3>INVITATIONS</h3><div class="mini-rule"></div>
    <p>Wedding, party and graduation invitations on soft recycled card with envelopes to match, ready in a few days.</p>
    <div class="spread">Spread the words</div><div class="row dots"><i class="dot"></i><i class="dot"></i><i class="dot"></i></div>
  </article>
  <article class="abs card" style="left:765px">
    <div class="card-img">IMAGE HERE</div><span class="btn-small">SEE MORE</span>
    <h3>FLYERS</h3><div class="mini-rule"></div>
    <p>Bright flyers for events, clubs and campaigns in any size, printed fast on glossy or matte paper in full colour.</p>
    <div class="spread">Spread the words</div><div class="row dots"><i class="dot"></i><i class="dot"></i><i class="dot"></i></div>
  </article>

  <div class="abs row view-all">View all products <svg width="24" height="20" viewBox="0 0 24 20"><path d="M1 10h20M13 2l8 8-8 8" fill="none" stroke="#1d1d1d" stroke-width="2.5"/></svg></div>
</section>

<section>
  <div class="abs quote-block">
    <div class="quote-box"><p>“ Save the<br>planet while<br>you can. ”</p></div>
    <div class="tweet"><i></i>Tweet this</div>
  </div>
  <div class="abs learn-block" role="img" aria-label="Print workshop with tables and machines">
    <h2>Learn how we do things</h2>
    <p>Can't find what you're looking for on our website? We<br>are happy to quote for unique and special printing.</p>
    <span class="btn-yellow">TELL US ABOUT YOUR PROJECT</span>
  </div>
</section>

<section class="abs subscribe">
  <div class="subscribe-photo" role="img" aria-label="Stationery mockup with notebook, cards and binder clips"></div>
  <h4>STAY UP TO DATE</h4>
  <small>Get the latest news about us</small>
  <div class="email-field"><svg width="10" height="7" viewBox="0 0 10 7"><rect width="10" height="7" fill="#888"/></svg>Email Address</div>
  <div class="btn-subscribe">SUBSCRIBE</div>
</section>

<section class="instagram">
  <h2 class="abs section-title" style="top:1888px">Check our Instagram page</h2>
  <div class="abs rule" style="top:1945px"></div>
  <p class="abs section-sub" style="top:1960px">Don't forget to leave a #VINDABORGPRENT</p>

  <div class="abs insta" style="left:88px"><div class="insta-img">IMAGE HERE</div><div class="insta-cap"><i></i><span>Fresh new artwork we print <b>@VINDABORGPRENT</b> #print #design #art</span></div></div>
  <div class="abs insta" style="left:300px"><div class="insta-img">IMAGE HERE</div><div class="insta-cap"><i></i><span>Fresh new artwork we print <b>@VINDABORGPRENT</b> #print #design #art</span></div></div>
  <div class="abs insta" style="left:514px"><div class="insta-img">IMAGE HERE</div><div class="insta-cap"><i></i><span>Fresh new artwork we print <b>@VINDABORGPRENT</b> #print #design #art</span></div></div>
  <div class="abs insta" style="left:726px"><div class="insta-img">IMAGE HERE</div><div class="insta-cap"><i></i><span>Fresh new artwork we print <b>@VINDABORGPRENT</b> #print #design #art</span></div></div>
  <div class="abs insta" style="left:938px"><div class="insta-img">IMAGE HERE</div><div class="insta-cap"><i></i><span>Fresh new artwork we print <b>@VINDABORGPRENT</b> #print #design #art</span></div></div>
</section>

<section class="contact">
  <div class="abs contact-dark">
    <div class="contact-col" style="left:75px"><h5>COME SEE US</h5>12 Lundargata, Vindaborg,<br>IS-101, Iceland</div>
    <div class="contact-col" style="left:249px"><h5>CONTACT US</h5>Tel: 555 0142<br>Monday to Friday from 9 am to 5 pm<br>Saturday from 10 am to 2 pm<br><br>verk@vindaborgprent.is</div>
  </div>
  <div class="abs map" role="img" aria-label="Street map showing the shop location"></div>

  <form class="abs form">
    <h4>You can also mail us directly. We'll get back<br>to you in a minute</h4>
    <label>Your name</label><div class="field">Name</div>
    <label>Your email address</label><div class="field">Email</div>
    <label>Message</label><div class="field tall">Type in your message</div>
    <div class="call">Or call us at +555 0142</div>
    <div class="btn-send">SEND</div>
  </form>
</section>

<div class="abs row partners">
  <span>Velora</span><span style="font-family:'Noto Serif',serif">KANTO</span><span style="font-weight:300">HILLMAN</span><span>EVERMORE</span><span style="font-weight:700;font-size:14px">Northline</span><span style="font-weight:300">Marsvik</span><span>L&amp;T</span>
</div>
<div class="abs footer-rule"></div>

<footer>
  <div class="abs footer-col" style="left:112px"><h6>ABOUT US</h6>About<br>Our Story</div>
  <div class="abs footer-col" style="left:300px"><h6>OUR OFFERS</h6>Art Print<br>Flyer<br>Invitation<br>Menu<br>Postcard<br>Poster</div>
  <div class="abs footer-col" style="left:476px"><h6>SHIPPING INFO</h6>Returns<br>Shipping<br>Taxes</div>
  <div class="abs row footer-social"><i class="dot"></i><i class="dot"></i><i class="dot"></i><i class="dot"></i><i class="dot"></i></div>
  <div class="abs copyright">© 2016-2017 Vindaborgprent. All Rights Reserved</div>
</footer>

</body>
</html>
```